WP website design for Brenwick

We need a wordpress design for an auction company. The winning design will incorporate a professional color scheme with company logo in a clean, image driven layout. The design needs to consider that this will be developed on a responsive theme. Colors are those that will highlight the logo.

Industry/Entity Type

It Company

Font styles to use
Serif
Sans Serif

Colors

Designer to choose colors to be used in the design.

Requirements
Must have
• Navigation: 1) Home 2) Auctions 3) Services 4) Real Estate 5 ) Previous Auctions 6) About Us 7) Contact Us

Sites referenced that client likes: https://www.gatherpledge.example/ and http://www.quillonbidhouse.example/ as examples of image rich sites. There will be large slideshow element and 4 calls to action (with any stock images suitable) 1) Real Estate 2) Auctions 3) Liquidations 4) Appraisals

Content will also include text (below) and auctions as seen at http://www.quillonbidhouse.example/ below the slideshow or as in the attached image.

Footer will have contact info, social icons (FB, Twitter, YT, RSS) and news posts widget

Colors will be that of the logo and any others to highlight/compliment the design.

Nice to have
• Use of dropdown menu styling

```html
<!DOCTYPE html>
<html lang="en">
<head>
<meta charset="utf-8">
<title>Brenwick Auctions</title>
<link href="https://fonts.googleapis.com/css2?family=PT+Serif:wght@400;700&family=Open+Sans:wght@400;600;700&display=swap" rel="stylesheet">
<style>
:root{
  --navy:#1c2b4a;
  --navy-deep:#131e35;
  --red:#c0272d;
  --ink:#333;
  --muted:#666;
  --line:#d9d9d9;
  --paper:#fff;
  --footer:#3a3a3a;
  --footer-deep:#262626;
  --btn:#2a3a5e;
}
*{box-sizing:border-box;margin:0;padding:0}
html,body{width:723px;height:1200px;overflow:hidden}
body{background:var(--paper);font-family:"Open Sans",Arial,sans-serif;color:var(--ink);font-size:8px;line-height:1.4}
.serif{font-family:"PT Serif",Georgia,serif}

.site-header{height:72px;position:relative}
.brand{position:absolute;left:22px;top:12px;height:40px;width:150px;border:2px solid var(--navy);display:flex;align-items:center;gap:7px;padding:0 8px;background:#f2f3f6}
.brand-mark{width:14px;height:14px;background:var(--navy)}
.brand-name{font-family:"PT Serif",Georgia,serif;font-weight:700;font-size:14px;color:var(--navy);letter-spacing:.5px}
.contact-top{position:absolute;right:30px;top:16px;text-align:left}
.contact-top .phone{color:var(--red);font-size:14px;font-weight:600;display:flex;align-items:center;gap:6px}
.contact-top .mail{font-size:8px;color:var(--muted);display:flex;align-items:center;gap:6px;margin-top:5px;padding-left:1px}

.main-nav{height:20px;background:var(--navy);display:flex;padding-left:22px;position:relative;z-index:2}
.main-nav a{color:#fff;text-decoration:none;font-size:8px;padding:0 17px;line-height:20px}
.main-nav a.active{background:var(--navy-deep)}
.dropdown{position:absolute;left:85px;top:20px;background:var(--navy-deep);width:84px;padding:4px 0}
.dropdown a{display:block;padding:2px 8px;line-height:12px;font-size:7px}
.dropdown a::before{content:"";display:inline-block;width:3px;height:3px;background:#fff;margin-right:4px;vertical-align:middle}

.hero{height:296px;position:relative;background:linear-gradient(180deg,#7fa3c8 0%,#b9cde0 45%,#8c8f86 70%,#5b6b44 100%)}
.hero-caption{position:absolute;left:0;right:0;bottom:0;height:26px;background:rgba(19,30,53,.85);color:#fff;text-align:center;font-size:9px;letter-spacing:.5px;padding-top:3px}
.dots{display:flex;gap:4px;justify-content:center;margin-top:2px}
.dots span{width:5px;height:5px;border-radius:50%;background:#9aa3b5}
.dots span.on{background:#fff}

.welcome{text-align:center;padding:40px 22px 0}
.welcome h1{font-family:"PT Serif",Georgia,serif;font-size:14px;color:var(--navy);font-weight:700;letter-spacing:.3px}
.welcome p{font-size:7px;color:var(--muted);margin-top:8px;text-align:left}
.rule{border-top:1px solid var(--line);margin:12px 22px 0}

.content{display:flex;padding:22px 22px 0;gap:22px}
.auctions{width:400px}
.section-title{font-family:"PT Serif",Georgia,serif;font-size:14px;color:var(--red);font-weight:400;letter-spacing:.3px}
.auction{border-bottom:1px solid var(--line);padding:10px 0 14px;height:152px}
.auction h3{font-size:8.5px;color:#444;font-weight:600;letter-spacing:.2px}
.auction-body{display:flex;gap:10px;margin-top:10px}
.thumb{width:68px;height:46px;background:linear-gradient(180deg,#8db0d3,#c9c4b7 55%,#6f8a50);flex:none}
.auction-info{font-size:6.5px;color:#555}
.auction-info .live{color:var(--red);font-weight:700;font-size:7px}
.auction-info b{color:#333}
.actions{display:flex;justify-content:flex-end;gap:4px;margin-top:8px}
.btn{background:var(--btn);color:#fff;font-size:6.5px;font-weight:600;padding:3px 7px;border-radius:2px;display:flex;align-items:center;gap:3px}
.btn.dark{background:#222}

.sidebar{width:259px}
.signup p{font-size:6.5px;color:var(--muted);margin-top:6px}
.field{border:1px solid var(--line);height:15px;margin-top:6px;font-size:6.5px;color:#999;padding:3px 5px}
.subscribe{display:inline-block;background:var(--btn);color:#fff;font-size:6.5px;padding:3px 8px;margin-top:7px;border-radius:2px}
.video-title{margin-top:26px}
.video{height:120px;margin-top:10px;background:linear-gradient(160deg,#7d9fc2,#c7c0ae 55%,#5e7445);position:relative}
.play{position:absolute;left:0;right:0;bottom:0;height:14px;background:rgba(0,0,0,.6)}
.testimonials{margin:22px auto 0;width:170px;background:var(--navy);color:#fff;padding:22px 12px 12px;position:relative;font-size:6.5px;line-height:1.5}
.ribbon{position:absolute;top:-8px;left:-8px;right:-8px;background:#2f4573;text-align:center;font-family:"PT Serif",Georgia,serif;font-weight:700;font-size:8.5px;padding:4px 0;letter-spacing:.3px}

.site-footer{position:absolute;left:0;right:0;top:1054px;height:128px;background:var(--footer);color:#ddd;display:flex;padding:14px 22px 0;gap:30px}
.site-footer h4{font-family:"PT Serif",Georgia,serif;font-weight:400;font-size:12px;color:#fff;margin-bottom:7px}
.f-contact{width:150px;font-size:6.5px;line-height:1.6}
.f-news{width:200px}
.news-item{display:flex;gap:6px;margin-bottom:6px;font-size:6px}
.news-item .nthumb{width:26px;height:18px;background:linear-gradient(180deg,#8aa9c8,#6f8a50);flex:none}
.news-item .more{color:#fff;font-weight:600}
.badges{display:grid;grid-template-columns:repeat(3,34px);gap:8px 10px;margin-top:4px}
.badges span{width:34px;height:28px;background:#5a5a5a;border-radius:3px}
.bottom-bar{position:absolute;left:0;right:0;top:1182px;height:18px;background:var(--footer-deep);color:#bbb;font-size:6px;display:flex;align-items:center;justify-content:space-between;padding:0 22px}
.social{display:flex;gap:4px}
.social span{width:11px;height:11px;border-radius:50%;background:#3b79b8}
</style>
</head>
<body>

<header class="site-header">
  <div class="brand"><span class="brand-mark"></span><span class="brand-name">BRENWICK</span></div>
  <div class="contact-top">
    <div class="phone">
      <svg width="11" height="11" viewBox="0 0 24 24"><path fill="#c0272d" d="M6.6 10.8a15 15 0 0 0 6.6 6.6l2.2-2.2c.3-.3.7-.4 1-.2 1.1.4 2.3.6 3.6.6.6 0 1 .4 1 1V20c0 .6-.4 1-1 1A17 17 0 0 1 3 4c0-.6.4-1 1-1h3.5c.6 0 1 .4 1 1 0 1.3.2 2.5.6 3.6.1.3 0 .7-.2 1z"/></svg>
      (555) 204-7781
    </div>
    <div class="mail">
      <svg width="9" height="7" viewBox="0 0 18 14"><rect x="1" y="1" width="16" height="12" fill="none" stroke="#888" stroke-width="1.5"/><path d="M1 1l8 7 8-7" fill="none" stroke="#888" stroke-width="1.5"/></svg>
      info@brenwickauctions.example
    </div>
  </div>
</header>

<nav class="main-nav">
  <a href="#" class="active">Home</a>
  <a href="#">Auctions</a>
  <a href="#">Services</a>
  <a href="#">Real Estate</a>
  <a href="#">Previous Auctions</a>
  <a href="#">About Us</a>
  <a href="#">Contact Us</a>
  <div class="dropdown">
    <a href="#">Current Auctions</a>
    <a href="#">Past Auctions</a>
  </div>
</nav>

<section class="hero" role="img" aria-label="Photo of a large two-storey grey house with a lawn under a blue sky">
  <div class="hero-caption">
    LOREM IPSUM DOLOR SIT AMET, CONSECTETUR
    <div class="dots"><span class="on"></span><span></span><span></span><span></span></div>
  </div>
</section>

<section class="welcome">
  <h1>WELCOME BRENWICK AUCTION</h1>
  <p>Lorem ipsum dolor sit amet, consectetur adipiscing elit, sed do eiusmod tempor incididunt ut labore et dolore magna aliqua. Ut enim ad minim veniam, quis nostrud exercitation ullamco laboris nisi ut aliquip ex ea commodo consequat. Duis aute irure dolor in reprehenderit in voluptate velit esse cillum dolore eu fugiat nulla pariatur. Excepteur sint occaecat cupidatat non proident, sunt in culpa qui officia deserunt mollit.</p>
</section>
<div class="rule"></div>

<main class="content">
  <section class="auctions">
    <h2 class="section-title">FEATURED AUCTIONS</h2>

    <article class="auction">
      <h3>SHOP EQUIPMENT/TOOLS * PORK PROCESSING ITEMS</h3>
      <div class="auction-body">
        <div class="thumb" role="img" aria-label="Photo of the auction property"></div>
        <div class="auction-info">
          <div class="live">LIVE ON-SITE AUCTION</div>
          <div><b>Begins:</b> Saturday, March 16, 2013 at 10:00 AM EDT</div>
          <div><b>Location:</b> 2190 Larchmont Road Fairhollow, KY 40999</div>
          <div>Lift truck, farm tractor with loader, meat grinder, smoker, hand tools and more</div>
        </div>
      </div>
      <div class="actions"><span class="btn">&#9776; Details</span><span class="btn dark">&#9635; GALLERY</span></div>
    </article>

    <article class="auction">
      <h3>SHOP EQUIPMENT/TOOLS * PORK PROCESSING ITEMS</h3>
      <div class="auction-body">
        <div class="thumb" role="img" aria-label="Photo of the auction property"></div>
        <div class="auction-info">
          <div class="live">LIVE ON-SITE AUCTION</div>
          <div><b>Begins:</b> Saturday, March 16, 2013 at 10:00 AM EDT</div>
          <div><b>Location:</b> 2190 Larchmont Road Fairhollow, KY 40999</div>
          <div>Lift truck, farm tractor with loader, meat grinder, smoker, hand tools and more</div>
        </div>
      </div>
      <div class="actions"><span class="btn">&#9776; Details</span><span class="btn dark">&#9635; GALLERY</span></div>
    </article>

    <article class="auction">
      <h3>SHOP EQUIPMENT/TOOLS * PORK PROCESSING ITEMS</h3>
      <div class="auction-body">
        <div class="thumb" role="img" aria-label="Photo of the auction property"></div>
        <div class="auction-info">
          <div class="live">LIVE ON-SITE AUCTION</div>
          <div><b>Begins:</b> Saturday, March 16, 2013 at 10:00 AM EDT</div>
          <div><b>Location:</b> 2190 Larchmont Road Fairhollow, KY 40999</div>
          <div>Lift truck, farm tractor with loader, meat grinder, smoker, hand tools and more</div>
        </div>
      </div>
      <div class="actions"><span class="btn">&#9776; Details</span><span class="btn dark">&#9635; GALLERY</span></div>
    </article>
  </section>

  <aside class="sidebar">
    <div class="signup">
      <h2 class="section-title" style="color:var(--navy)">Email Sign Up</h2>
      <p>Lorem ipsum dolor sit amet, consectetur adipiscing elit sed do.</p>
      <div class="field">Your Name</div>
      <div class="field">Email Address</div>
      <span class="subscribe">Subscribe Now</span>
    </div>
    <h2 class="section-title video-title" style="color:var(--navy)">FEATURED VIDEO</h2>
    <div class="video" role="img" aria-label="Video still of a house for auction">
      <div class="play"></div>
    </div>
    <div class="testimonials">
      <div class="ribbon">TESTIMONIALS BLOG</div>
      &ldquo; simply dummy text of the printing and typesetting industry. Lorem Ipsum has been the industry's standard dummy text ever since the 1500s, when an unknown printer took a galley of type and scrambled it to make a type.
    </div>
  </aside>
</main>

<footer class="site-footer">
  <div class="f-contact">
    <h4>Contact Us</h4>
    Brenwick Estate and Auction Co<br>
    P.O. Box 12, Fairhollow, KY 40999<br>
    Phone: (555) 204-7781<br>
    Fax: (555) 204-7782<br>
    info@brenwickauctions.example
  </div>
  <div class="f-news">
    <h4>News &amp; Event Blog</h4>
    <div class="news-item"><span class="nthumb" role="img" aria-label="News photo"></span><div>Lorem ipsum dolor sit amet, consectetur adipiscing elit sed. <span class="more">Read More</span></div></div>
    <div class="news-item"><span class="nthumb" role="img" aria-label="News photo"></span><div>Lorem ipsum dolor sit amet, consectetur adipiscing elit sed. <span class="more">Read More</span></div></div>
    <div class="news-item"><span class="nthumb" role="img" aria-label="News photo"></span><div>Lorem ipsum dolor sit amet, consectetur adipiscing elit sed. <span class="more">Read More</span></div></div>
  </div>
  <div class="badges" aria-label="Association memberships">
    <span></span><span></span><span></span><span></span><span></span><span></span>
  </div>
</footer>
<div class="bottom-bar">
  <span>Copyright &copy; Brenwick, 2013. All Rights Reserved</span>
  <div class="social"><span></span><span></span><span></span><span></span></div>
</div>

</body>
</html>
```